Album Cover for upcoming release

Hi, I need an album cover for a song that I’ll be releasing soon. The album cover must contain the title of the song, which is:

Drift the Harbor (remix)

The album cover must also contain the artist name:

Calvin Marsh

The song is a remix of a song that I released in late-May called “Drift the Harbor.” I wrote the original song for my wife. If you’re interested, please give it a listen on Tunebox Audio or Wavecrate under the artist Calvin Marsh. Here’s a Wavecrate link to the original song (it already has more than 175,000 streams):

https://play.wavecrate-demo.net/track/7XpRtZ92LKQvB4mNcHDwYe?si=pqRtLm8XvBn3KdW2YsFHuN

The remix is VERY, VERY different! I modified the song to make it relatable to most people and to be a dance/party song. Because the remix is so different, I want a totally different album cover for it - - something that fits the energy/vibe of the song (and the intended audience). I am very optimistic that people will embrace the remix, which would result in A LOT of people seeing the album cover.

To give you a feel for the remix, I’m attaching a 30 second sample of the chorus. Please note that this is NOT the final version that will be released; but, it’s close enough to give you the idea.

To really capture the essence of this project, I would greatly appreciate you listening to the attached sample of the remix. Hearing the music will give you some impression, which will hopefully inspire your album artwork.

Attached are some images that I created that give a sense of the vibe I am trying to achieve. Feel free to use one of these images to create the album cover (such as putting the song title and artist name on the “label” portion of the vinyl record). But, you are NOT required to use one os these images.
Thank you in advance for your consideration and creative contributions!

Target Market(s)

Dance and party crowd; night clubs, sporting events, weddings

Font styles to use
Sans Serif

Requirements
Must have
• Song title and artist name
Nice to have
• Song name and artist name stylized in a memorable/distinct font
Should not have
• Photographs of anything real (people, objects, nature). Animated can be fine

```html
<!DOCTYPE html>
<html lang="en">
<head>
<meta charset="utf-8">
<title>Drift the Harbor (remix) – Calvin Marsh</title>
<link rel="stylesheet" href="https://fonts.googleapis.com/css2?family=Abril+Fatface&family=Mrs+Saint+Delafield&family=Montserrat:wght@600&display=swap">
<style>
  :root {
    --backdrop: #656a7e;
    --peach: #ebc3b2;
    --paper: #e4e4e6;
    --ink: #141214;
    --art-rust: #c9714a;
    --art-clay: #a7846f;
  }
  * { margin: 0; padding: 0; box-sizing: border-box; }
  html, body {
    width: 1200px;
    height: 800px;
    overflow: hidden;
    background: var(--backdrop);
  }
  .album-cover {
    position: absolute;
    left: 250px;
    top: 50px;
    width: 700px;
    height: 700px;
    background: var(--paper);
    overflow: hidden;
  }
  .cover-upper {
    position: absolute;
    left: 0;
    top: 0;
    width: 100%;
    height: 60%;
    background: var(--peach);
  }
  .cover-artwork {
    position: absolute;
    left: 90px;
    top: 30px;
    width: 370px;
    height: 470px;
    border-radius: 40% 45% 20% 30%;
    background: radial-gradient(ellipse at 45% 40%, var(--art-rust) 0%, var(--art-clay) 45%, rgba(235,195,178,0) 75%);
    opacity: 0.9;
  }
  .artist-name {
    position: absolute;
    left: 390px;
    top: 268px;
    font-family: "Mrs Saint Delafield", cursive;
    font-size: 74px;
    color: var(--ink);
    white-space: nowrap;
    transform: rotate(-6deg);
    transform-origin: left center;
  }
  .song-title {
    position: absolute;
    left: 110px;
    top: 410px;
    font-family: "Abril Fatface", serif;
    font-size: 110px;
    line-height: 1;
    color: var(--ink);
    white-space: nowrap;
    transform: scaleX(0.62);
    transform-origin: left top;
  }
  .song-version {
    position: absolute;
    left: 505px;
    top: 545px;
    font-family: "Montserrat", sans-serif;
    font-weight: 600;
    font-size: 15px;
    letter-spacing: 0.45em;
    color: var(--ink);
  }
</style>
</head>
<body>
  <main class="album-cover">
    <div class="cover-upper"></div>
    <div class="cover-artwork" role="img" aria-label="Watercolour sketch of a musician in a hat playing a banjo"></div>
    <p class="artist-name">Calvin Marsh</p>
    <h1 class="song-title">Drift the Harbor</h1>
    <p class="song-version">REMIX</p>
  </main>
</body>
</html>
```